Bright Lantern Film Production Website

Hi! I need to remake our website design. We want it to be closer to the template we picked http://pixelmarket.example/item/orion-multipurpose-responsive-theme/full_screen_preview/8342961

Here is what we have for now:
http://brightlanternfilm.example/
http://www.brightlanternfilm.example/bright-lantern-film-about-us-2/
http://www.brightlanternfilm.example/services/
http://www.brightlanternfilm.example/bright-lantern-film-company-page/
http://www.brightlanternfilm.example/bright-lantern-film-contact-us/
http://www.brightlanternfilm.example/bright-lantern-film-careers-page/

I would be very grateful for suggestions and new design.

Thanks!
Marisol

Target Market(s)

Startups and companies in need for commercials and promo videos

Industry/Entity Type

Video Production

Number of Pages Required

5+ page

Requirements
Must have
• We want to set the tone of an artistic atmosphere and innovational culture.

```html
<!DOCTYPE html>
<html lang="en">
<head>
<meta charset="utf-8">
<title>Bright Lantern Film Production – Services</title>
<link href="https://fonts.googleapis.com/css2?family=Raleway:wght@300;400;500&family=Open+Sans:wght@400&display=swap" rel="stylesheet">
<style>
  :root{
    --brand-red:#8b0000;
    --icon-red:#c40a0a;
    --icon-ring:#a80000;
    --ink:#111;
    --heading:#444;
    --body:#666;
    --footer-bg:#232323;
    --footer-bottom:#1c1c1c;
    --footer-text:#ddd;
    --footer-muted:#bbb;
    --white:#fff;
  }
  *{margin:0;padding:0;box-sizing:border-box}
  html,body{width:1039px;height:1200px;overflow:hidden;background:var(--white)}
  body{position:relative;font-family:"Open Sans",Arial,sans-serif;color:var(--body)}

  .site-header{position:absolute;left:0;top:0;width:1039px;height:92px;background:var(--brand-red)}
  .brand{position:absolute;left:156px;top:19px;display:flex;align-items:center;gap:12px}
  .brand-mark{width:52px;height:52px;border:3px solid var(--white);border-radius:50%}
  .brand-name{font-family:"Raleway",sans-serif;font-weight:300;font-size:15px;letter-spacing:3px;color:var(--white)}
  .main-nav{position:absolute;top:0;left:0}
  .nav-item{position:absolute;top:42px;font-family:"Raleway",sans-serif;font-weight:500;font-size:12.5px;color:var(--white);white-space:nowrap}
  .nav-active-ring{position:absolute;left:530px;top:8px;width:76px;height:76px;border:3px solid var(--white);border-radius:50%}
  .search-icon{position:absolute;left:855px;top:40px}

  .hero{position:absolute;left:0;top:92px;width:1039px;height:222px;
    background:linear-gradient(100deg,#b9b5b0 0%,#d3d0cb 30%,#2a2b2e 45%,#cfcfcf 62%,#e2dedb 78%,#3a2a22 90%,#1c1614 100%)}
  .hero-title{position:absolute;left:159px;top:104px;font-family:"Raleway",sans-serif;font-weight:500;font-size:29px;color:var(--ink)}

  .services{position:absolute;left:0;top:314px;width:1039px}
  .services-heading{position:absolute;left:156px;top:38px;font-family:"Raleway",sans-serif;font-weight:400;font-size:23px;color:var(--heading)}
  .services-intro{position:absolute;left:159px;top:76px;width:715px;font-size:9.5px;line-height:17.3px;color:var(--body)}

  .service{position:absolute;width:360px;height:90px}
  .service-icon{position:absolute;left:0;top:0;width:82px;height:82px}
  .service-title{position:absolute;left:93px;top:7px;font-family:"Raleway",sans-serif;font-weight:400;font-size:16.5px;color:var(--ink)}
  .service-text{position:absolute;left:93px;top:33px;width:255px;font-size:9.5px;line-height:17.3px;color:var(--body)}

  .site-footer{position:absolute;left:0;top:917px;width:1039px;height:283px;background:var(--footer-bg);border-top:5px solid #b00}
  .footer-brand{position:absolute;left:140px;top:44px;width:202px;text-align:center}
  .footer-mark{width:88px;height:88px;border:4px solid var(--white);border-radius:50%;margin:0 auto}
  .footer-name{margin-top:17px;font-family:"Raleway",sans-serif;font-weight:300;font-size:14.5px;letter-spacing:3px;color:var(--white);white-space:nowrap}
  .footer-col{position:absolute;top:50px}
  .footer-heading{font-family:"Raleway",sans-serif;font-weight:500;font-size:13px;color:var(--white);margin-bottom:14px}
  .post-title{font-size:11px;color:var(--footer-text);margin-bottom:3px}
  .post-text{font-size:8px;line-height:13.5px;color:var(--footer-muted);margin-bottom:16px;width:205px}
  .contact-text{font-size:8px;line-height:13.5px;color:var(--footer-muted);width:150px;margin-bottom:6px}
  .contact-line{display:flex;align-items:center;gap:5px;font-size:11px;color:var(--footer-text);margin-bottom:5px}
  .social{display:flex;gap:2px}
  .social span{width:24px;height:24px;border:1.5px solid var(--white);border-radius:50%}
  .footer-bottom{position:absolute;left:0;top:233px;width:1039px;height:50px;background:var(--footer-bottom)}
  .copyright{position:absolute;left:164px;top:20px;font-size:9.5px;color:var(--footer-muted)}
</style>
</head>
<body>

<header class="site-header">
  <div class="brand"><div class="brand-mark"></div><span class="brand-name">BRIGHT LANTERN FILM</span></div>
  <nav class="main-nav">
    <span class="nav-item" style="left:459px">HOME</span>
    <div class="nav-active-ring"></div>
    <span class="nav-item" style="left:538px">SERVICES</span>
    <span class="nav-item" style="left:639px">WE ARE HIRING</span>
    <span class="nav-item" style="left:773px">CONTACT</span>
    <svg class="search-icon" width="18" height="18" viewBox="0 0 18 18"><circle cx="7.5" cy="7.5" r="5.5" fill="none" stroke="#fff" stroke-width="2.6"/><line x1="11.5" y1="11.5" x2="16" y2="16" stroke="#fff" stroke-width="3" stroke-linecap="round"/></svg>
  </nav>
</header>

<section class="hero" role="img" aria-label="Photo of hands typing on a laptop at an outdoor café table with a glass">
  <h1 class="hero-title">OUR SERVICES</h1>
</section>

<main class="services">
  <h2 class="services-heading">OUR SERVICES</h2>
  <p class="services-intro">Mauris vel lacus vitae felis vestibulum volutpat E&nbsp; eu imperdiet ac nisl Cum sociis natoque penatibus et magnis dis parturient montes nascetur ridiculus&nbsp; mus In iaculis facilisis massa Etiam eu urna Sed porta Suspendisse quam leo molestie sed luctus quis feugiat in pede Fusce tellus Sed metus augue convallis et vehicula ut pulvinar eu ante Integer orci tellus tristique vitae consequat nec Vivamus porttitor purus nisi eleifend libero a tempus</p>

  <article class="service" style="left:155px;top:155px">
    <svg class="service-icon" viewBox="0 0 82 82"><circle cx="41" cy="41" r="41" fill="var(--icon-red)"/><circle cx="41" cy="41" r="33" fill="var(--icon-ring)"/><circle cx="41" cy="41" r="30" fill="var(--icon-red)"/>
      <path d="M52 27 C44 27 38 32 34 40 L29 40 L25 45 L32 45 L37 50 L37 57 L42 53 L42 48 C50 44 55 38 55 30 Z" fill="#fff"/><circle cx="47" cy="35" r="3" fill="var(--icon-red)"/></svg>
    <h3 class="service-title">Service Tittle</h3>
    <p class="service-text">Sed porta Suspendisse quam leo molestie sed luctus quis feugiat in pede Fusce tellus Sed metus augue convallis et vehicula ut pulvinar eu ante Integer orci</p>
  </article>

  <article class="service" style="left:522px;top:155px">
    <svg class="service-icon" viewBox="0 0 82 82"><circle cx="41" cy="41" r="41" fill="var(--icon-red)"/><circle cx="41" cy="41" r="33" fill="var(--icon-ring)"/><circle cx="41" cy="41" r="30" fill="var(--icon-red)"/>
      <rect x="20" y="25" width="42" height="28" fill="none" stroke="#fff" stroke-width="2.5"/><polygon points="37,32 37,46 47,39" fill="#fff"/><line x1="33" y1="57" x2="49" y2="57" stroke="#fff" stroke-width="2"/></svg>
    <h3 class="service-title">Service Tittle</h3>
    <p class="service-text">Sed porta Suspendisse quam leo molestie sed luctus quis feugiat in pede Fusce tellus Sed metus augue convallis et vehicula ut pulvinar eu ante Integer orci</p>
  </article>

  <article class="service" style="left:155px;top:278px">
    <svg class="service-icon" viewBox="0 0 82 82"><circle cx="41" cy="41" r="41" fill="var(--icon-red)"/><circle cx="41" cy="41" r="33" fill="var(--icon-ring)"/><circle cx="41" cy="41" r="30" fill="var(--icon-red)"/>
      <rect x="19" y="22" width="17" height="11" rx="2" fill="none" stroke="#fff" stroke-width="1.8"/><circle cx="23.5" cy="27.5" r="1.2" fill="#fff"/><circle cx="27.5" cy="27.5" r="1.2" fill="#fff"/><circle cx="31.5" cy="27.5" r="1.2" fill="#fff"/>
      <circle cx="47" cy="31" r="7" fill="none" stroke="#fff" stroke-width="2"/><path d="M33 57 L35 46 Q47 39 59 46 L61 57 Z" fill="none" stroke="#fff" stroke-width="2"/></svg>
    <h3 class="service-title">Service Tittle</h3>
    <p class="service-text">Sed porta Suspendisse quam leo molestie sed luctus quis feugiat in pede Fusce tellus Sed metus augue convallis et vehicula ut pulvinar eu ante Integer orci</p>
  </article>

  <article class="service" style="left:522px;top:278px">
    <svg class="service-icon" viewBox="0 0 82 82"><circle cx="41" cy="41" r="41" fill="var(--icon-red)"/><circle cx="41" cy="41" r="33" fill="var(--icon-ring)"/><circle cx="41" cy="41" r="30" fill="var(--icon-red)"/>
      <rect x="24" y="31" width="27" height="20" rx="3" fill="#fff"/><polygon points="52,39 61,32 61,50 52,43" fill="#fff"/></svg>
    <h3 class="service-title">Service Tittle</h3>
    <p class="service-text">Sed porta Suspendisse quam leo molestie sed luctus quis feugiat in pede Fusce tellus Sed metus augue convallis et vehicula ut pulvinar eu ante Integer orci</p>
  </article>

  <article class="service" style="left:155px;top:402px">
    <svg class="service-icon" viewBox="0 0 82 82"><circle cx="41" cy="41" r="41" fill="var(--icon-red)"/><circle cx="41" cy="41" r="33" fill="var(--icon-ring)"/><circle cx="41" cy="41" r="30" fill="var(--icon-red)"/>
      <path d="M27 36 L36 36 L55 27 L55 55 L36 46 L27 46 Z" fill="#fff"/><path d="M31 46 L35 46 L38 55 L34 55 Z" fill="#fff"/></svg>
    <h3 class="service-title">Service Tittle</h3>
    <p class="service-text">Sed porta Suspendisse quam leo molestie sed luctus quis feugiat in pede Fusce tellus Sed metus augue convallis et vehicula ut pulvinar eu ante Integer orci</p>
  </article>

  <article class="service" style="left:522px;top:402px">
    <svg class="service-icon" viewBox="0 0 82 82"><circle cx="41" cy="41" r="41" fill="var(--icon-red)"/><circle cx="41" cy="41" r="33" fill="var(--icon-ring)"/><circle cx="41" cy="41" r="30" fill="var(--icon-red)"/>
      <rect x="26" y="22" width="30" height="38" fill="#fff"/><rect x="34" y="25" width="14" height="14" fill="var(--icon-red)"/><rect x="34" y="43" width="14" height="14" fill="var(--icon-red)"/>
      <g fill="var(--icon-red)"><rect x="28" y="25" width="3" height="4"/><rect x="28" y="33" width="3" height="4"/><rect x="28" y="41" width="3" height="4"/><rect x="28" y="49" width="3" height="4"/><rect x="51" y="25" width="3" height="4"/><rect x="51" y="33" width="3" height="4"/><rect x="51" y="41" width="3" height="4"/><rect x="51" y="49" width="3" height="4"/></g></svg>
    <h3 class="service-title">Service Tittle</h3>
    <p class="service-text">Sed porta Suspendisse quam leo molestie sed luctus quis feugiat in pede Fusce tellus Sed metus augue convallis et vehicula ut pulvinar eu ante Integer orci</p>
  </article>
</main>

<footer class="site-footer">
  <div class="footer-brand"><div class="footer-mark"></div><div class="footer-name">BRIGHT LANTERN FILM</div></div>

  <div class="footer-col" style="left:362px">
    <h4 class="footer-heading">RECENT POSTS</h4>
    <p class="post-title">Cum sociis natoque penatibus</p>
    <p class="post-text">magnis dis parturient montes nascetur ridiculus mus In iaculis facilisis massa Etiam eu urna</p>
    <p class="post-title">Duis quam Nam eget</p>
    <p class="post-text">magnis dis parturient montes nascetur ridiculus mus In iaculis facilisis massa Etiam eu urna</p>
  </div>

  <div class="footer-col" style="left:588px">
    <h4 class="footer-heading">CONTACT INFO</h4>
    <p class="contact-text">magnis dis parturient montes nascetur ridiculus mus In iaculis facilisis</p>
    <p class="contact-line"><svg width="11" height="9" viewBox="0 0 11 9"><rect width="11" height="9" fill="#fff"/><path d="M0 0 L5.5 5 L11 0" fill="none" stroke="#232323" stroke-width="1.2"/></svg>info@brightlanternfilm.example</p>
    <p class="contact-line"><svg width="11" height="11" viewBox="0 0 11 11"><path d="M2 0 L4 3 L3 4.5 Q4.5 7 6.5 8 L8 7 L11 9 L9.5 11 Q3 10 0 2 Z" fill="#fff"/></svg>+15550142087</p>
  </div>

  <div class="footer-col" style="left:763px">
    <h4 class="footer-heading">FOLLOW US</h4>
    <div class="social"><span></span><span></span><span></span><span></span></div>
  </div>

  <div class="footer-bottom"><p class="copyright">© 2016 Company Name&nbsp; All right reserved&nbsp; Term of Use</p></div>
</footer>

</body>
</html>
```